Popup Banners - BrightCounsel - Legal Technology

- We need two banners (same style) designed with two different images and different text.

- The details of the printing requirements are attached, along with suggested images.

- The banners should share the same theme as our website www.brightcounsel.com.au

- The first banner would include our logo (attached), use the 'roads join' image (attached) in some way and text: New Opportunities - Where legal services and technology meet.

- The second banner would include our logo (attached), use the 'jigsaw' image (attached) in some way and use text: Legal Technology Strategy, Advice and Capability.

- Details on what are required from the Printer is attached also.

Target Market(s)

Legal Professionals

Industry/Entity Type

Information Technology

Font styles to use
Sans Serif

Requirements
Must have
• Our logo (attached), suggested text and the image mentioned for each.
Nice to have
• Professional and modern look
Should not have
• Cheap looking

```html
<!DOCTYPE html>
<html lang="en">
<head>
<meta charset="utf-8">
<title>BrightCounsel Popup Banners</title>
<link rel="stylesheet" href="https://fonts.googleapis.com/css2?family=Arimo:wght@400&display=swap">
<style>
  :root {
    --stage: #7f97aa;
    --navy: #0d2a52;
    --navy-deep: #0a2146;
    --white: #ffffff;
    --sky-blue: #5b9bd5;
    --swoosh-grey: #8c8c8c;
    --brand-grey: #4a4a4a;
    --glow: #dbe7f5;
    --grass: #5d7f3a;
    --grass-dark: #3f5a28;
    --haze: #7a8f9e;
  }
  * { margin: 0; padding: 0; box-sizing: border-box; }
  html, body { width: 1200px; height: 1200px; overflow: hidden; }
  body {
    background: var(--stage);
    font-family: "Arimo", Arial, sans-serif;
    position: relative;
  }
  .banner {
    position: absolute;
    top: 140px;
    width: 400px;
    height: 920px;
    background: var(--navy);
    overflow: hidden;
  }
  .banner--strategy { left: 150px; }
  .banner--opportunities { left: 650px; }

  .banner__headline {
    position: absolute;
    top: 52px;
    right: 30px;
    width: 300px;
    text-align: right;
    color: var(--white);
    font-size: 21px;
    line-height: 1.2;
    font-weight: 400;
  }

  .banner__photo { position: absolute; left: 0; width: 100%; }
  .banner__photo--jigsaw {
    top: 250px;
    height: 380px;
    background: radial-gradient(ellipse 42% 40% at 52% 45%, var(--glow) 0%, #6f95c6 22%, #1c4479 50%, rgba(13,42,82,0) 78%);
  }
  .banner__photo--roads {
    top: 430px;
    height: 420px;
    background: linear-gradient(to bottom, var(--navy) 0%, var(--haze) 14%, var(--grass) 26%, var(--grass-dark) 100%);
  }

  .banner__sweep {
    position: absolute;
    left: 0;
    top: 0;
    width: 400px;
    height: 920px;
  }

  .brand {
    position: absolute;
    left: 34px;
    bottom: 38px;
    display: flex;
    align-items: center;
    gap: 10px;
  }
  .brand__mark {
    width: 12px;
    height: 12px;
    background: var(--sky-blue);
  }
  .brand__name {
    color: var(--brand-grey);
    font-size: 18px;
    letter-spacing: 3px;
  }
</style>
</head>
<body>

  <section class="banner banner--strategy">
    <h2 class="banner__headline">Legal Technology Strategy Advice and Capability</h2>
    <div class="banner__photo banner__photo--jigsaw" role="img" aria-label="Hand placing a glowing jigsaw puzzle piece against a dark blue background"></div>
    <svg class="banner__sweep" viewBox="0 0 300 690" preserveAspectRatio="none" aria-hidden="true">
      <path d="M0,455 C40,560 150,622 300,618 L300,690 L0,690 Z" fill="var(--white)"/>
      <path d="M0,490 C50,560 120,592 195,606 C120,598 45,572 0,512 Z" fill="var(--navy)"/>
      <path d="M205,656 C240,652 275,658 300,670" fill="none" stroke="var(--sky-blue)" stroke-width="2.2"/>
      <path d="M215,664 C245,661 275,666 300,678" fill="none" stroke="var(--swoosh-grey)" stroke-width="1.4"/>
    </svg>
    <div class="brand">
      <span class="brand__mark"></span>
      <span class="brand__name">BrightCounsel</span>
    </div>
  </section>

  <section class="banner banner--opportunities">
    <h2 class="banner__headline">New Opportunities - Where Legal Services and Technology Meet</h2>
    <div class="banner__photo banner__photo--roads" role="img" aria-label="Two gravel roads joining across a green grassy hill"></div>
    <svg class="banner__sweep" viewBox="0 0 300 690" preserveAspectRatio="none" aria-hidden="true">
      <path d="M0,455 C40,560 150,622 300,618 L300,690 L0,690 Z" fill="var(--white)"/>
      <path d="M0,490 C50,560 120,592 195,606 C120,598 45,572 0,512 Z" fill="var(--navy)"/>
      <path d="M205,656 C240,652 275,658 300,670" fill="none" stroke="var(--sky-blue)" stroke-width="2.2"/>
      <path d="M215,664 C245,661 275,666 300,678" fill="none" stroke="var(--swoosh-grey)" stroke-width="1.4"/>
    </svg>
    <div class="brand">
      <span class="brand__mark"></span>
      <span class="brand__name">BrightCounsel</span>
    </div>
  </section>

</body>
</html>
```